Create a Graphic About YOURSELF and PixelHarbor

PixelHarbor would like you (designers) to create an awesome graphic to promote YOURSELF and your profile on PixelHarbor!

Your graphic should communicate your name, your services and should mention PixelHarbor.

The design should be perfect for sharing on Chatterly. Here's an example of what we'd like http://blog.pixelharbor-example.ca/article/333/pixelharbor-launches-3000-hire-me-social-design-contest

Once you submitted your design, we'd love you to share the design ('advertisement') and promote yourself and PixelHarbor to your friends and potential customers. So make your submissions great and get your friends to vote for your design by 'Liking' it on Chatterly!

Prizes:
$1500 - "PixelHarbor Community" prize awarded to the designer with the most Chatterly 'Likes'
5 x $50 for the next 5 'most liked' designs on Chatterly

$1000 - "Hire Me" prize awarded to the designer who receives the most client invites
5 x $50 for the next 5 'most invited' designers

In summary, this is a great opportunity for you to increase your exposure to PixelHarbor customers and win cash prizes. Show off your design skills and get hired by PixelHarbor customers from around the world!

Target Market(s)

Fans, friends and customers of YOU

Industry/Entity Type

Cash

Requirements
Must have
• 1) Include your PixelHarbor user name on the graphic so customers can find you in the PixelHarbor Designer Directory
2) Include the tagline "Hire Me on PixelHarbor.com!" in your graphic design.
3) Share your design's URL on our Chatterly wall at http://chatterly-example.com/pixelharbor and get your friends to 'like' your design.
Nice to have
• 1) Include a tagline that expresses your design approach/philosophy
2) Artwork dimensions: 403 x 403 px
3) You can submit more than 1 design!
Should not have
• You must own the copyright of any images you use including stock imagery.

```html
<!DOCTYPE html>
<html lang="en">
<head>
<meta charset="utf-8">
<title>NightCrane – Hire me on PixelHarbor</title>
<link rel="stylesheet" href="https://fonts.googleapis.com/css2?family=Oswald:wght@700&family=Gochi+Hand&family=Great+Vibes&family=Questrial&display=swap">
<style>
  :root {
    --bg-deep: #0b171b;
    --bg-mid: #14252b;
    --stripe: #263840;
    --stripe-light: #34474f;
    --circle: #1c2e35;
    --accent-blue: #4ba3c6;
    --soft-grey: #a4a8aa;
    --pure-white: #ffffff;
    --ornament-grey: #5a6b72;
  }
  html, body {
    margin: 0;
    padding: 0;
    width: 1200px;
    height: 900px;
    overflow: hidden;
    background: var(--bg-deep);
  }
  .poster {
    position: relative;
    width: 1200px;
    height: 900px;
    overflow: hidden;
    background: radial-gradient(ellipse at 40% 45%, var(--bg-mid) 0%, var(--bg-deep) 70%);
    font-family: "Questrial", sans-serif;
  }
  .backdrop {
    position: absolute;
    inset: 0;
  }
  .artwork {
    position: absolute;
  }
  .artwork--flourish-left {
    left: 40px;
    top: 30px;
    width: 620px;
    height: 420px;
    border-radius: 40px;
    background: radial-gradient(ellipse at 50% 55%, rgba(90,107,114,0.30) 0%, rgba(90,107,114,0.12) 50%, transparent 78%);
  }
  .artwork--cube {
    left: 190px;
    top: 330px;
    width: 400px;
    height: 425px;
    border-radius: 24px;
    background: linear-gradient(180deg, rgba(75,163,198,0.75) 0%, rgba(75,163,198,0.55) 35%, rgba(200,205,208,0.55) 50%, rgba(190,196,199,0.45) 100%);
  }
  .artwork--butterfly {
    left: 735px;
    top: 215px;
    width: 125px;
    height: 120px;
    border-radius: 50%;
    background: radial-gradient(circle, rgba(75,163,198,0.45) 0%, rgba(75,163,198,0.15) 55%, transparent 72%);
  }
  .artwork--flourish-right {
    left: 1020px;
    top: 490px;
    width: 170px;
    height: 210px;
    border-radius: 30px;
    background: radial-gradient(ellipse at 50% 55%, rgba(255,255,255,0.22) 0%, rgba(75,163,198,0.12) 50%, transparent 75%);
  }
  .artwork--flower-bottom {
    left: 815px;
    top: 630px;
    width: 110px;
    height: 110px;
    border-radius: 50%;
    background: radial-gradient(circle, rgba(90,107,114,0.55) 0%, rgba(90,107,114,0.2) 60%, transparent 75%);
  }
  .motto {
    position: absolute;
    left: 0;
    top: 0;
    width: 1200px;
    height: 470px;
    margin: 0;
    font-weight: 400;
  }
  .motto span {
    position: absolute;
    display: block;
    line-height: 1;
    white-space: nowrap;
  }
  .motto__lead {
    left: 716px;
    top: 62px;
    font-size: 88px;
    color: var(--accent-blue);
    letter-spacing: 1px;
  }
  .motto__grey {
    font-size: 46px;
    color: var(--soft-grey);
    letter-spacing: 0.5px;
  }
  .motto__line-will { left: 724px; top: 162px; }
  .motto__script {
    left: 856px;
    top: 188px;
    font-family: "Great Vibes", cursive;
    font-size: 96px;
    color: var(--accent-blue);
  }
  .motto__line-itself { left: 974px; top: 276px; }
  .motto__line-depth { left: 724px; top: 342px; }
  .motto__closing {
    left: 716px;
    top: 390px;
    font-size: 66px;
    color: var(--pure-white);
    letter-spacing: 0.5px;
  }
  .services {
    position: absolute;
    left: 30px;
    top: 742px;
    margin: 0;
    padding: 0;
    list-style: none;
  }
  .services__item {
    display: flex;
    align-items: center;
    font-family: "Oswald", sans-serif;
    font-weight: 700;
    font-size: 31px;
    color: var(--pure-white);
    height: 45px;
    letter-spacing: 1px;
  }
  .services__item::before {
    content: "";
    width: 15px;
    height: 15px;
    border-radius: 50%;
    background: var(--accent-blue);
    margin-right: 16px;
  }
  .signoff {
    position: absolute;
    right: 26px;
    top: 718px;
    width: 320px;
    text-align: right;
  }
  .signoff__username {
    font-family: "Oswald", sans-serif;
    font-weight: 700;
    font-size: 46px;
    color: var(--accent-blue);
    line-height: 1.1;
    display: block;
    letter-spacing: 0.5px;
  }
  .signoff__invite {
    font-family: "Gochi Hand", cursive;
    font-size: 54px;
    color: var(--pure-white);
    line-height: 1.05;
    display: block;
  }
  .signoff__platform {
    display: inline-flex;
    align-items: center;
    gap: 10px;
    font-size: 36px;
    color: var(--pure-white);
    margin-top: 4px;
  }
  .signoff__dot {
    width: 26px;
    height: 26px;
    border-radius: 50%;
    background: var(--accent-blue);
  }
</style>
</head>
<body>
<main class="poster">
  <svg class="backdrop" width="1200" height="900" viewBox="0 0 1200 900" aria-hidden="true">
    <circle cx="410" cy="110" r="95" fill="var(--circle)" opacity="0.8"/>
    <circle cx="160" cy="370" r="100" fill="var(--circle)" opacity="0.6"/>
    <circle cx="780" cy="240" r="60" fill="var(--circle)" opacity="0.5"/>
    <circle cx="800" cy="570" r="75" fill="var(--circle)" opacity="0.6"/>
    <circle cx="190" cy="640" r="60" fill="var(--circle)" opacity="0.5"/>
    <circle cx="530" cy="780" r="75" fill="var(--circle)" opacity="0.5"/>
    <g fill="var(--stripe)">
      <rect x="0" y="470" width="1200" height="10"/>
      <rect x="0" y="488" width="1200" height="4"/>
      <rect x="0" y="500" width="1200" height="12"/>
      <rect x="0" y="522" width="1200" height="5"/>
      <rect x="0" y="540" width="1200" height="40" fill="var(--stripe-light)" opacity="0.55"/>
      <rect x="0" y="590" width="1200" height="6"/>
      <rect x="0" y="604" width="1200" height="12"/>
      <rect x="0" y="626" width="1200" height="5"/>
      <rect x="0" y="640" width="1200" height="3"/>
    </g>
  </svg>

  <div class="artwork artwork--flourish-left" role="img" aria-label="Grey floral swirls with daisies and blue butterflies"></div>
  <div class="artwork artwork--cube" role="img" aria-label="Puzzle cube with a blue top face and white sides casting a shadow"></div>
  <div class="artwork artwork--butterfly" role="img" aria-label="Blue butterfly"></div>
  <div class="artwork artwork--flower-bottom" role="img" aria-label="Grey daisy flower"></div>
  <div class="artwork artwork--flourish-right" role="img" aria-label="White floral swirl with small blue butterflies"></div>

  <h1 class="motto">
    <span class="motto__lead">Originality</span>
    <span class="motto__grey motto__line-will">will always</span>
    <span class="motto__script">surface</span>
    <span class="motto__grey motto__line-itself">itself</span>
    <span class="motto__grey motto__line-depth">from the depth of</span>
    <span class="motto__closing">commonality</span>
  </h1>

  <ul class="services">
    <li class="services__item">Corporate Identity</li>
    <li class="services__item">Graphic Design</li>
    <li class="services__item">Print Design</li>
  </ul>

  <div class="signoff">
    <span class="signoff__username">NightCrane</span>
    <span class="signoff__invite">Hire me on</span>
    <span class="signoff__platform"><span class="signoff__dot"></span>PixelHarbor</span>
  </div>
</main>
</body>
</html>
```